Business Consulting Business Card

professional business card with basic information (1) First and Last name (2) email address, (3) phone number, (4) website.

```html
<!DOCTYPE html>
<html lang="en">
<head>
<meta charset="utf-8">
<title>Tidewell Business Card</title>
<link href="https://fonts.googleapis.com/css2?family=Lato:wght@400;700;900&display=swap" rel="stylesheet">
<style>
  :root {
    --backdrop: #5f5f5f;
    --navy: #0b2a40;
    --navy-deep: #092538;
    --navy-pattern: #0f3450;
    --aqua: #3fb3cd;
    --ink-light: #e8eef2;
    --rule: #1f5a78;
  }
  * { margin: 0; padding: 0; box-sizing: border-box; }
  html, body {
    width: 1200px; height: 900px; overflow: hidden;
    background: var(--backdrop);
    font-family: "Lato", sans-serif;
  }
  .canvas {
    width: 1200px; height: 900px;
    display: flex; align-items: center; justify-content: center; gap: 50px;
  }
  .card {
    position: relative;
    width: 540px; height: 310px;
    background: var(--navy);
    box-shadow: 0 10px 30px rgba(0,0,0,0.35);
    overflow: hidden;
  }
  .brand {
    display: flex; align-items: center; gap: 12px;
    color: var(--ink-light);
    font-weight: 400; letter-spacing: 0.28em;
  }
  .brand-dot {
    border-radius: 50%;
    background: var(--aqua);
    flex: none;
  }
  /* front */
  .card-front .brand {
    position: absolute; left: 44px; top: 118px;
    font-size: 21px;
  }
  .card-front .brand-dot { width: 30px; height: 30px; }
  .divider {
    position: absolute; left: 262px; top: 70px;
    width: 1px; height: 170px; background: var(--rule);
  }
  .contact {
    position: absolute; left: 290px; top: 62px;
    color: var(--ink-light);
  }
  .person-name {
    color: var(--aqua); font-weight: 900;
    font-size: 27px; letter-spacing: 0.01em; line-height: 1;
  }
  .person-title { font-size: 15px; margin-top: 6px; }
  .address { font-size: 15px; line-height: 1.35; margin-top: 8px; }
  .channels { list-style: none; margin-top: 8px; font-size: 15px; line-height: 1.45; }
  .channels li { display: flex; align-items: center; gap: 9px; }
  .channels svg { width: 14px; height: 14px; flex: none; }
  /* back */
  .card-back { background: var(--navy-deep); }
  .pattern-field {
    position: absolute; inset: 0;
    background: linear-gradient(135deg, var(--navy-pattern), var(--navy-deep));
  }
  .card-back .brand {
    position: absolute; left: 50%; top: 50%;
    transform: translate(-50%, -50%);
    font-size: 28px;
  }
  .card-back .brand-dot { width: 40px; height: 40px; }
</style>
</head>
<body>
<main class="canvas">
  <section class="card card-front">
    <div class="brand"><span class="brand-dot"></span><span class="brand-name">TIDEWELL</span></div>
    <div class="divider"></div>
    <div class="contact">
      <h1 class="person-name">MARCUS HALE</h1>
      <p class="person-title">Founder &amp; CEO</p>
      <p class="address">48 Harbour View Road<br>Suite 210, Portland ME</p>
      <ul class="channels">
        <li>
          <svg viewBox="0 0 16 16" aria-hidden="true"><path d="M4 1.5 6 4.5 4.8 6a8 8 0 0 0 5.2 5.2L11.5 10l3 2-1.2 2.5C7.5 14.5 1.5 8.5 1.5 2.7Z" fill="var(--aqua)"/></svg>
          <span>207 555 0148</span>
        </li>
        <li>
          <svg viewBox="0 0 16 16" aria-hidden="true"><rect x="1" y="3" width="14" height="10" fill="var(--aqua)"/><path d="M1 3 8 9 15 3" stroke="var(--navy)" stroke-width="1.4" fill="none"/></svg>
          <span>marcus@tidewell.co</span>
        </li>
        <li>
          <svg viewBox="0 0 16 16" aria-hidden="true"><circle cx="8" cy="8" r="6.5" fill="none" stroke="var(--aqua)" stroke-width="1.4"/><ellipse cx="8" cy="8" rx="2.8" ry="6.5" fill="none" stroke="var(--aqua)" stroke-width="1.2"/><path d="M1.5 8h13" stroke="var(--aqua)" stroke-width="1.2"/></svg>
          <span>www.tidewell.co</span>
        </li>
      </ul>
    </div>
  </section>

  <section class="card card-back">
    <div class="pattern-field" role="img" aria-label="Repeating tonal pattern of the brand symbol across the card back"></div>
    <div class="brand"><span class="brand-dot"></span><span class="brand-name">TIDEWELL</span></div>
  </section>
</main>
</body>
</html>
```